Modern/Bold/Unique Prenatal Vitamin label redesign

We are in need of a design update for our Prenatal Vitamin label. We want to modernize our label and give it a fresh feel.
It should bring a feeling of fun, joy, and sophistication, but also be bold/edgy/unique and portray Trust and Authority. Our buyers are mainly mothers in the age range of 25-34 who are pregnant or breastfeeding.
I will attach our current label design, as well as some inspiration to go off of.
We like the idea of having a clean, easy to read label label with bold/vibrant colors and fonts. We like the idea of having some retro vibes in it as well
Please see the attached artwork for design inspiration (New Design Idea). We like the idea of having a pregnant mother image like the attachment on the label, with the rest of the label being white. Please come up with a unique drawing/image for the design. We cannot use a copied image or stock image.
We look forward to working with you!

```html
<!DOCTYPE html>
<html lang="en">
<head>
<meta charset="utf-8">
<title>Cradle Plus – Prenatal Multivitamin Label</title>
<link rel="stylesheet" href="https://fonts.googleapis.com/css2?family=DM+Serif+Display&family=Poppins:wght@400;500;600&display=swap">
<style>
  :root {
    --backdrop: #ececee;
    --label: #ffffff;
    --brand-rose: #c2185b;
    --title-pink: #e5197a;
    --teal: #1f8c8c;
    --art-red: #e2452f;
    --art-orange: #f0a02a;
    --art-teal: #1aa3a3;
  }
  * { margin: 0; padding: 0; box-sizing: border-box; }
  html, body {
    width: 1200px;
    height: 1200px;
    overflow: hidden;
    background: var(--backdrop);
  }
  .label {
    position: absolute;
    left: 160px;
    top: 50px;
    width: 880px;
    height: 1100px;
    background: var(--label);
    box-shadow: 0 2px 14px rgba(0,0,0,0.06);
  }
  .brand {
    position: absolute;
    left: 65px;
    top: 96px;
    display: flex;
    align-items: center;
    gap: 10px;
    font-family: "DM Serif Display", serif;
    font-size: 54px;
    line-height: 1;
    color: var(--brand-rose);
  }
  .brand-dot {
    width: 16px;
    height: 16px;
    border-radius: 50%;
    background: var(--brand-rose);
    margin-top: -22px;
  }
  .product-title {
    position: absolute;
    left: 62px;
    top: 372px;
    font-family: "Poppins", sans-serif;
    font-weight: 600;
    font-size: 82px;
    line-height: 0.98;
    color: var(--title-pink);
    letter-spacing: 0.5px;
  }
  .tagline {
    position: absolute;
    left: 65px;
    top: 580px;
    font-family: "Poppins", sans-serif;
    font-weight: 400;
    font-size: 25px;
    line-height: 37px;
    color: var(--teal);
    text-transform: uppercase;
  }
  .tagline strong { font-weight: 600; }
  .count {
    position: absolute;
    left: 62px;
    top: 842px;
    display: flex;
    align-items: center;
    gap: 8px;
  }
  .count-number {
    font-family: "Poppins", sans-serif;
    font-weight: 500;
    font-size: 66px;
    line-height: 1;
    color: var(--brand-rose);
  }
  .count-unit {
    background: var(--title-pink);
    color: #fff;
    font-family: "Poppins", sans-serif;
    font-weight: 500;
    font-size: 17px;
    line-height: 19px;
    padding: 4px 10px;
  }
  .supplement-note {
    position: absolute;
    left: 65px;
    top: 926px;
    font-family: "Poppins", sans-serif;
    font-weight: 600;
    font-size: 19px;
    color: var(--brand-rose);
  }
  .mother-art {
    position: absolute;
    left: 414px;
    top: 144px;
    width: 440px;
    height: 936px;
    border-radius: 180px 180px 120px 200px;
    background:
      radial-gradient(circle at 70% 30%, rgba(240,160,42,0.7), transparent 45%),
      radial-gradient(circle at 35% 70%, rgba(26,163,163,0.45), transparent 40%),
      linear-gradient(160deg, var(--art-red), #c73324 60%, var(--art-orange));
  }
</style>
</head>
<body>
  <main class="label">
    <div class="brand"><span>nestling co.</span><span class="brand-dot"></span></div>

    <h1 class="product-title">CRADLE<br>PLUS</h1>

    <p class="tagline">Once daily<br>Premium multi vitamin<br>For <strong>Mama &amp; Baby</strong></p>

    <div class="count">
      <span class="count-number">90</span>
      <span class="count-unit">Veggie<br>Capsules</span>
    </div>
    <p class="supplement-note">Dietary Supplements</p>

    <div class="mother-art" role="img" aria-label="Paint-splatter illustration of a pregnant mother's silhouette in red, orange, yellow and teal"></div>
  </main>
</body>
</html>
```